Book cover needed for a major new book on emotional resilience

The book will be titled: 'Stone to Stream: from habit bound to builders of renewal - The guide for growing steady teams and institutions'
My websites are http://www.pathmorrow.com and http://www.lumbrava.org and I am http://en.wikiverse-sample.org/wiki/Martin_Okonedo_(uncertainty_scholar) ad expert in developing emotional resilience. My previous book was The Murky Dividend.
The premise of the book is to introduce brand new material which is the first ever methodology and strategy on how to develop emotional resilience across entire populations like organisations and companies or moving people from fear about change to finding flow through resilience.
The final design should communicate the fact that this is a strategy and methodology. That it is about developing people and entire organisations to be more resilient and who are able to deal with change better.
Target Market(s)
Consultants, Organisational development consultants, Human Resource professionals.

```html
<!DOCTYPE html>
<html lang="en">
<head>
<meta charset="utf-8">
<title>Stone to Stream — Book Cover</title>
<link rel="stylesheet" href="https://fonts.googleapis.com/css2?family=Open+Sans:wght@300;400&display=swap">
<style>
  :root {
    --page-bg: #eceeed;
    --cover-white: #ffffff;
    --cover-grey: #e6e6e6;
    --cover-edge: #c9c9c9;
    --frame-green: #1cf21c;
    --ink-green: #1a6d1a;
    --title-dark: #1e7a1e;
    --title-light: #3ef06a;
    --step-green: #22ee33;
    --step-label: #2fe84a;
    --seal-green: #3dfc5a;
    --seal-ink: #1b3a1b;
    --art-light: #7dfa8c;
    --art-dark: #2a8a35;
  }
  * { margin: 0; padding: 0; box-sizing: border-box; }
  html, body {
    width: 1200px;
    height: 1023px;
    overflow: hidden;
    background: var(--page-bg);
  }
  .stage {
    position: relative;
    width: 1200px;
    height: 1023px;
    display: flex;
    align-items: center;
    justify-content: center;
  }
  .book-cover {
    width: 698px;
    height: 1000px;
    border: 1px solid var(--cover-edge);
    border-radius: 6px;
    background: linear-gradient(100deg, var(--cover-white) 0%, var(--cover-white) 45%, var(--cover-grey) 100%);
    box-shadow: 0 6px 24px rgba(0,0,0,0.12);
    overflow: hidden;
  }
  .book-cover svg { display: block; width: 100%; height: 100%; }
  .author { font-family: "Open Sans", sans-serif; font-weight: 400; font-size: 25px; fill: var(--ink-green); }
  .title { font-family: "Open Sans", sans-serif; font-weight: 400; font-size: 70px; }
  .subtitle { font-family: "Open Sans", sans-serif; font-weight: 400; font-size: 22px; fill: var(--ink-green); }
  .step-label { font-family: "Open Sans", sans-serif; font-weight: 400; font-size: 29px; fill: var(--step-label); }
  .seal-text { font-family: "Open Sans", sans-serif; font-weight: 300; font-size: 15px; fill: var(--seal-ink); text-anchor: middle; }
  .frame-line { fill: none; stroke: var(--frame-green); stroke-width: 5; stroke-linecap: round; }
  .staircase { fill: none; stroke: var(--step-green); stroke-width: 12; stroke-linejoin: miter; }
</style>
</head>
<body>
<main class="stage">
  <article class="book-cover">
    <svg viewBox="0 0 604 865" xmlns="http://www.w3.org/2000/svg">
      <defs>
        <linearGradient id="title-fill" x1="0" x2="1" y1="0" y2="0">
          <stop offset="0" stop-color="var(--title-dark)"/>
          <stop offset="1" stop-color="var(--title-light)"/>
        </linearGradient>
        <radialGradient id="art-fill" cx="0.45" cy="0.4" r="0.7">
          <stop offset="0" stop-color="var(--art-light)"/>
          <stop offset="1" stop-color="var(--art-dark)"/>
        </radialGradient>
        <filter id="seal-glow" x="-20%" y="-20%" width="140%" height="140%">
          <feGaussianBlur stdDeviation="6"/>
        </filter>
      </defs>

      <path class="frame-line" d="M4 11 C300 11 430 22 505 48 Q565 72 565 160 L563 323"/>
      <path class="frame-line" d="M5 806 Q6 856 52 856 L242 857"/>

      <text class="author" x="18" y="113">martin okonedo</text>

      <ellipse class="butterfly-art" role="img" aria-label="Illustration of a green butterfly resting at an angle"
               cx="465" cy="262" rx="78" ry="88" fill="url(#art-fill)"/>

      <text class="title" x="20" y="430" textLength="522" lengthAdjust="spacingAndGlyphs" fill="url(#title-fill)">STONE TO STREAM</text>
      <text class="subtitle" x="22" y="468" textLength="520" lengthAdjust="spacingAndGlyphs">from habit bound to builders of renewal</text>

      <path class="staircase" d="M125 782 L125 685 L240 685 L240 580 L350 580 L350 488 L433 488"/>
      <text class="step-label" x="148" y="716">step1</text>
      <text class="step-label" x="246" y="633">step2</text>
      <text class="step-label" x="350" y="531">step3</text>

      <ellipse class="caterpillar-art" role="img" aria-label="Illustration of a green caterpillar climbing the first step"
               cx="143" cy="676" rx="48" ry="22" fill="url(#art-fill)"/>
      <ellipse class="cocoon-art" role="img" aria-label="Illustration of a caterpillar emerging with wings on the second step"
               cx="243" cy="572" rx="42" ry="32" fill="url(#art-fill)"/>

      <g class="seal">
        <circle cx="482" cy="740" r="122" fill="var(--seal-green)" opacity="0.55" filter="url(#seal-glow)"/>
        <circle cx="482" cy="740" r="118" fill="var(--seal-green)"/>
        <text class="seal-text" x="482" y="722">THE GUIDE FOR GROWING</text>
        <text class="seal-text" x="482" y="744">STEADY TEAMS</text>
        <text class="seal-text" x="482" y="766">AND INSTITUTIONS</text>
      </g>
    </svg>
  </article>
</main>
</body>
</html>
```